Hip-Hop Artist TM Blaze Needs a Album Cover Design

I need an album cover design for my upcoming album. I am a hip-hop artist from Seattle, WA. I have been writing/producing/releases music for the past 15 years. This will be my 4th full length album. For examples of my previous album cover designs and single designs go here --> www.tmblaze-music.net. The title of the album is called "Quiet Harbors". It is an emotional, inspirational album with 18 songs that I wrote and produced over the past 3 years. Some track titles include - "Hold Fast", "Golden Dust". "Kings of Tomorrow", "Burn The Ledger", & "Edge of Winter". I would like the cover to contain something design pattern based, 1 idea would be the blueprint design of a mind processing thoughts - abstract I know. But, feel free to think creatively or out of the box on this as I don't want to give too much direction - you are the graphic artist, not me. I have typically had blues, grays, and blacks in my album covers, but I don't want to put limits on the approach an artist wants to take. Feel free to take this in a direction you think would be interesting.

Reason: I would like to extend the deadline for design submissions in order to have time to provide appropriate feedback to the designers.

Reason: Thank you to everyone that has submitted designs thus far. I truly appreciate you taking the time and sharing your creativity. With the recent design submissions that came in today + the revisions sent yesterday/today, I would like to extend this contest by 5 days - as this album + design means the world to me. I will be providing feedback to the top designers tomorrow. Thank you all again!

```html
<!DOCTYPE html>
<html lang="en">
<head>
<meta charset="utf-8">
<title>Quiet Harbors — TM Blaze</title>
<link rel="stylesheet" href="https://fonts.googleapis.com/css2?family=Archivo+Black&display=swap">
<style>
  :root {
    --night: #0a0b22;
    --night-deep: #060717;
    --web-glow: #2a4550;
    --web-line: #5b7480;
    --title-white: #f4f6ff;
    --title-violet: #3b3fd0;
    --glitch-grey: rgba(200, 205, 225, 0.55);
    --signature-white: #f2f2f2;
  }

  * { margin: 0; padding: 0; box-sizing: border-box; }

  html, body {
    width: 1200px;
    height: 1200px;
    overflow: hidden;
    background: var(--night);
  }

  .album-cover {
    position: relative;
    width: 1200px;
    height: 1200px;
    overflow: hidden;
    background: radial-gradient(circle at 50% 50%, var(--night) 0%, var(--night-deep) 100%);
  }

  .neural-web {
    position: absolute;
    inset: 0;
    background:
      radial-gradient(ellipse 380px 420px at 560px 560px, rgba(42, 69, 80, 0.55) 0%, rgba(42, 69, 80, 0.18) 55%, transparent 80%),
      radial-gradient(ellipse 700px 260px at 900px 60px, rgba(91, 116, 128, 0.12) 0%, transparent 75%),
      radial-gradient(ellipse 600px 300px at 200px 1050px, rgba(91, 116, 128, 0.10) 0%, transparent 75%);
  }

  .glitch-bands {
    position: absolute;
    inset: 0;
  }

  .album-title {
    position: absolute;
    left: 0;
    right: 0;
    top: 360px;
    text-align: center;
    font-family: "Archivo Black", "Arial Black", sans-serif;
    font-size: 150px;
    line-height: 186px;
    letter-spacing: 4px;
    text-transform: uppercase;
  }

  .album-title__line {
    display: block;
    color: transparent;
    background: repeating-linear-gradient(
      to bottom,
      var(--title-white) 0px,
      var(--title-white) 6px,
      rgba(244, 246, 255, 0.15) 6px,
      rgba(244, 246, 255, 0.15) 9px
    );
    -webkit-background-clip: text;
    background-clip: text;
    filter: drop-shadow(-4px 2px 0 var(--title-violet)) drop-shadow(0 0 10px rgba(59, 63, 208, 0.45));
  }

  .album-title__line--second {
    padding-left: 10px;
  }

  .artist-name {
    position: absolute;
    right: 62px;
    bottom: 70px;
    font-family: "Archivo Black", "Arial Black", sans-serif;
    font-size: 50px;
    line-height: 1;
    letter-spacing: 1px;
    color: var(--signature-white);
  }
</style>
</head>
<body>
  <main class="album-cover">
    <div class="neural-web" role="img" aria-label="Abstract network of thin connected lines and nodes forming a glowing cluster around the title"></div>

    <svg class="glitch-bands" width="1200" height="1200" viewBox="0 0 1200 1200" aria-hidden="true">
      <g fill="var(--glitch-grey)">
        <rect x="16" y="388" width="170" height="7"/>
        <rect x="30" y="410" width="150" height="5"/>
        <rect x="20" y="432" width="175" height="8"/>
        <rect x="44" y="456" width="140" height="5"/>
        <rect x="24" y="476" width="160" height="6"/>
        <rect x="1030" y="390" width="150" height="6"/>
        <rect x="1045" y="414" width="135" height="5"/>
        <rect x="1020" y="438" width="165" height="7"/>
        <rect x="1040" y="462" width="120" height="5"/>
        <rect x="30" y="586" width="14" height="62"/>
        <rect x="80" y="592" width="140" height="5"/>
        <rect x="66" y="616" width="160" height="7"/>
        <rect x="96" y="640" width="120" height="5"/>
        <rect x="1010" y="596" width="160" height="6"/>
        <rect x="1030" y="620" width="140" height="7"/>
        <rect x="1018" y="644" width="150" height="5"/>
      </g>
    </svg>

    <h1 class="album-title">
      <span class="album-title__line">Quiet</span>
      <span class="album-title__line album-title__line--second">Harbors</span>
    </h1>

    <p class="artist-name">TM Blaze</p>
  </main>
</body>
</html>
```